Test and Tag business card design

We are an appliance test and tag company in Brisbane Australia requiring a business card design.
I don't have a logo.
Card front: Matte black background with white font.
Card back: White background with black font colour
Examples are attached
Minimalist design
Reason: Looking for more designs with an extreme minimal feel
Industry/Entity Type
Appliance
Contact Information for Business Card
Business name: Summit Check and Label
Description: Onsite Electrical Testing and Tagging
Licence No. 48213
Name: Greg Palmby
Mobile: 0417 592 348
Email: greg@summitcheckandlabel.com.au
Web: summitcheckandlabel.com.au
Logo Text
Summit Check and Label
Look and feel

```html
<!DOCTYPE html>
<html lang="en">
<head>
<meta charset="utf-8">
<title>Summit Check and Label – Business Card</title>
<link rel="stylesheet" href="https://fonts.googleapis.com/css2?family=Lato:ital,wght@0,400;0,700;0,900;1,400&display=swap">
<style>
  :root {
    --page-bg: #ededed;
    --card-black: #000000;
    --card-teal: #1a97b0;
    --text-white: #ffffff;
    --text-grey: #8a8a8a;
    --card-shadow: rgba(0, 0, 0, 0.35);
  }
  html, body {
    margin: 0;
    width: 1200px;
    height: 1000px;
    overflow: hidden;
    background: var(--page-bg);
  }
  .canvas {
    position: relative;
    width: 1200px;
    height: 1000px;
  }
  .card {
    position: absolute;
    left: 141px;
    top: 235px;
    width: 917px;
    height: 529px;
    background: var(--card-teal);
    box-shadow: 3px 4px 6px var(--card-shadow);
    overflow: hidden;
    font-family: "Lato", Arial, sans-serif;
    color: var(--text-white);
  }
  .card__top {
    position: absolute;
    left: 0; top: 0;
    width: 100%;
    height: 305px;
    background: var(--card-black);
  }
  .card__stripe {
    position: absolute;
    left: 0;
    width: 100%;
    height: 3px;
    background: var(--card-teal);
  }
  .card__stripe--one { top: 287px; }
  .card__stripe--two { top: 295px; }
  .card__artwork {
    position: absolute;
    left: 560px;
    top: 0;
    width: 330px;
    height: 529px;
  }
  .brand {
    position: absolute;
    left: 56px;
    top: 137px;
  }
  .brand__name {
    margin: 0;
    font-weight: 700;
    font-size: 27px;
    letter-spacing: 0.3px;
    line-height: 34px;
    text-transform: uppercase;
  }
  .brand__tagline {
    margin: 2px 0 0;
    font-style: italic;
    font-size: 22px;
    line-height: 30px;
  }
  .brand__licence {
    margin: 2px 0 0;
    font-size: 17px;
    line-height: 24px;
    color: var(--text-grey);
  }
  .contact {
    position: absolute;
    left: 56px;
    top: 330px;
  }
  .contact__name {
    margin: 0 0 8px;
    font-weight: 700;
    font-size: 33px;
    line-height: 42px;
  }
  .contact__list {
    list-style: none;
    margin: 0;
    padding: 0;
  }
  .contact__item {
    display: flex;
    align-items: center;
    height: 36px;
    font-size: 21px;
  }
  .contact__icon {
    width: 24px;
    height: 24px;
    margin-right: 10px;
    flex: none;
  }
</style>
</head>
<body>
<div class="canvas">
  <div class="card">
    <div class="card__top"></div>
    <div class="card__stripe card__stripe--one"></div>
    <div class="card__stripe card__stripe--two"></div>

    <svg class="card__artwork" role="img" aria-label="White branching lightning bolt striking down across the card" viewBox="0 0 330 529">
      <defs>
        <linearGradient id="boltGlow" x1="0" y1="0" x2="0" y2="1">
          <stop offset="0" stop-color="#ffffff" stop-opacity="0.16"/>
          <stop offset="0.55" stop-color="#ffffff" stop-opacity="0.22"/>
          <stop offset="1" stop-color="#ffffff" stop-opacity="0.08"/>
        </linearGradient>
      </defs>
      <rect width="330" height="529" fill="url(#boltGlow)"/>
    </svg>

    <div class="brand">
      <h1 class="brand__name">Summit Check and Label</h1>
      <p class="brand__tagline">Onsite Electrical Testing and Tagging</p>
      <p class="brand__licence">Licence No. 48213</p>
    </div>

    <div class="contact">
      <h2 class="contact__name">Greg Palmby</h2>
      <ul class="contact__list">
        <li class="contact__item">
          <svg class="contact__icon" viewBox="0 0 24 24" aria-hidden="true">
            <rect x="1" y="1" width="22" height="22" rx="5" fill="#fff"/>
            <path d="M9 5 h3 v4 h-2 v6 h2 v4 h-3 q-3 0 -3 -3 v-8 q0 -3 3 -3z" fill="var(--card-teal)"/>
          </svg>
          <span>0417 592 348</span>
        </li>
        <li class="contact__item">
          <svg class="contact__icon" viewBox="0 0 24 24" aria-hidden="true">
            <rect x="1" y="1" width="22" height="22" rx="5" fill="#fff"/>
            <path d="M6 12 h12 M18 12 a6 6 0 1 0 -1.5 4" stroke="var(--card-teal)" stroke-width="2.6" fill="none"/>
          </svg>
          <span>greg@summitcheckandlabel.com.au</span>
        </li>
        <li class="contact__item">
          <svg class="contact__icon" viewBox="0 0 24 24" aria-hidden="true">
            <rect x="1" y="1" width="22" height="22" rx="5" fill="#fff"/>
            <path d="M4.5 6 l3.5 12 l4 -9 l4 9 l3.5 -12" stroke="var(--card-teal)" stroke-width="2.6" fill="none" stroke-linejoin="round"/>
          </svg>
          <span>www.summitcheckandlabel.com.au</span>
        </li>
      </ul>
    </div>
  </div>
</div>
</body>
</html>
```